The RotaHarbor Podcast - A top rated podcast for criminal justice professionals

A top rated criminal justice podcast. A show about criminal justice topics, self-help, education and becoming a better you. Created and Hosted by -Dorian Weatherall.

Dorian Weatherall is a retired Police Commander from Colorado with over two decades of experience in many different roles. He is also an adjunct college professor and enjoys teaching the next generation of criminal justice professionals. Dorian holds advanced degrees in Business and Organizational Leadership. A former Army Paratrooper with the elite 47th Ridgeline Brigade, Dorian is an avid supporter of active military members and veterans.

www.rotaharbor-example.com

Target Market(s)

Criminal Justice Professionals. Entrepreneurs, Leaders, Fitness Expert, Well Being experts.

Industry/Entity Type

Police

Font styles to use
Serif

Colors

Designer to choose colors to be used in the design.

Requirements
Must have
• American Flag. Microphone & Headphones
Nice to have
• Thin blue line - A symbol for law enforcement
Should not have
• N/A

```html
<!DOCTYPE html>
<html lang="en">
<head>
<meta charset="UTF-8">
<title>The RotaHarbor Podcast</title>
<link rel="stylesheet" href="https://fonts.googleapis.com/css2?family=Lato:wght@400;700;900&family=Great+Vibes&display=swap">
<style>
  :root {
    --red: #a3192c;
    --red-dark: #7d0f1f;
    --navy: #27327d;
    --blue: #3847a0;
    --blue-mid: #5566b8;
    --blue-soft: #c9cfea;
    --paper: #f4f5fb;
    --white: #ffffff;
  }
  * { margin: 0; padding: 0; box-sizing: border-box; }
  html, body { width: 849px; height: 1200px; overflow: hidden; background: var(--white); }
  .poster {
    position: relative;
    width: 849px;
    height: 1200px;
    overflow: hidden;
    background: linear-gradient(180deg, var(--paper) 0%, var(--white) 60%, #eef0f8 100%);
    font-family: "Lato", sans-serif;
  }
  .flag-backdrop {
    position: absolute; left: 0; top: 0; width: 849px; height: 300px;
    background:
      linear-gradient(180deg, rgba(255,255,255,0) 40%, rgba(244,245,251,1) 100%),
      linear-gradient(90deg, #33448f 0%, #6a78b8 30%, #e9c3c8 55%, #c95a68 80%, #f2dfe2 100%);
    opacity: .85;
  }
  .shapes { position: absolute; inset: 0; }
  .title {
    position: absolute; left: 322px; top: 128px; width: 440px;
    color: var(--white); font-weight: 700; font-size: 62px; line-height: 1.12; text-align: center;
  }
  .tagline {
    position: absolute; left: 52px; top: 345px; width: 760px;
    color: var(--white); font-weight: 400; font-size: 40px; line-height: 1.2;
  }
  .tagline .cap { font-size: 58px; }
  .description {
    position: absolute; left: 80px; top: 722px; width: 690px;
    color: var(--navy); font-size: 22px; line-height: 1.3; text-align: center;
  }
  .host-photo {
    position: absolute; left: 527px; top: 870px; width: 296px; height: 282px;
    background: linear-gradient(135deg, #b9c0cf 0%, #7d8493 45%, #3d4150 100%);
    border: 4px solid var(--white);
  }
  .host-name {
    position: absolute; left: 548px; top: 1080px; width: 260px;
    font-family: "Great Vibes", cursive; color: var(--white); font-size: 36px; text-align: center;
  }
  .host-label {
    position: absolute; left: 548px; top: 1124px; width: 260px;
    color: var(--white); font-size: 10px; letter-spacing: 2px; text-align: center; font-weight: 700;
  }
  .credit {
    position: absolute; left: 46px; top: 1080px;
    color: var(--red); font-size: 24px; line-height: 1.3; font-weight: 400;
  }
</style>
</head>
<body>
<main class="poster">
  <div class="flag-backdrop" role="img" aria-label="Faded American flag waving across the top"></div>

  <svg class="shapes" width="849" height="1200" viewBox="0 0 849 1200" aria-hidden="true">
    <!-- blue tagline field -->
    <polygon points="0,290 849,250 849,700 0,700" fill="var(--blue)"/>
    <polygon points="420,280 849,230 849,520 640,520" fill="var(--blue-mid)" opacity=".45"/>
    <!-- red title ribbon -->
    <polygon points="0,110 780,98 830,200 780,300 0,300" fill="var(--red)"/>
    <polygon points="0,250 780,240 780,300 0,300" fill="var(--red-dark)" opacity=".6"/>
    <!-- sound wave -->
    <g fill="var(--white)">
      <rect x="40"  y="196" width="6" height="12" rx="3"/>
      <rect x="54"  y="186" width="6" height="32" rx="3"/>
      <rect x="68"  y="176" width="6" height="52" rx="3"/>
      <rect x="82"  y="160" width="6" height="84" rx="3"/>
      <rect x="96"  y="150" width="6" height="104" rx="3"/>
      <rect x="110" y="170" width="6" height="64" rx="3"/>
      <rect x="124" y="182" width="6" height="40" rx="3"/>
      <rect x="138" y="164" width="6" height="76" rx="3"/>
      <rect x="152" y="178" width="6" height="48" rx="3"/>
      <rect x="166" y="190" width="6" height="24" rx="3"/>
      <rect x="180" y="196" width="6" height="12" rx="3"/>
      <rect x="194" y="199" width="80" height="6" rx="3"/>
    </g>
    <!-- light band behind the icon strip -->
    <rect x="0" y="540" width="849" height="180" fill="var(--paper)"/>
    <!-- icon blocks -->
    <rect x="0" y="575" width="270" height="110" fill="var(--blue)"/>
    <rect x="580" y="575" width="269" height="110" fill="var(--blue)"/>
    <!-- flag stripes -->
    <rect x="270" y="575" width="310" height="110" fill="var(--white)"/>
    <g fill="var(--red)">
      <rect x="270" y="575" width="310" height="13"/>
      <rect x="270" y="599" width="310" height="13"/>
      <rect x="270" y="623" width="310" height="13"/>
      <rect x="270" y="647" width="310" height="13"/>
      <rect x="270" y="672" width="310" height="13"/>
    </g>
    <!-- headphones icon -->
    <g stroke="var(--white)" stroke-width="6" fill="none" stroke-linecap="round">
      <path d="M108 640 v-12 a26 26 0 0 1 52 0 v12"/>
    </g>
    <g fill="var(--white)">
      <rect x="100" y="634" width="14" height="24" rx="5"/>
      <rect x="154" y="634" width="14" height="24" rx="5"/>
    </g>
    <!-- microphone icon -->
    <g fill="none" stroke="var(--white)" stroke-width="5" stroke-linecap="round">
      <path d="M694 622 v8 a18 18 0 0 0 36 0 v-8"/>
      <line x1="712" y1="648" x2="712" y2="662"/>
      <line x1="700" y1="662" x2="724" y2="662"/>
    </g>
    <rect x="702" y="596" width="20" height="42" rx="10" fill="var(--white)"/>
    <!-- diagonal accent toward the bottom -->
    <polygon points="0,810 849,760 849,1200 0,1200" fill="#e8ebf6" opacity=".6"/>
    <!-- left rule lines -->
    <g stroke="var(--blue)" stroke-width="4" stroke-linecap="round">
      <line x1="46" y1="838" x2="398" y2="838"/>
      <line x1="46" y1="866" x2="300" y2="866"/>
      <line x1="46" y1="894" x2="230" y2="894"/>
    </g>
    <!-- thin blue line -->
    <line x1="0" y1="1188" x2="849" y2="1188" stroke="var(--navy)" stroke-width="4"/>
  </svg>

  <h1 class="title">RotaHarbor Podcast</h1>
  <p class="tagline"><span class="cap">A</span> top rated podcast for criminal justice professionals</p>
  <p class="description">A show about criminal justice topics, self-help, education and becoming a better you</p>

  <div class="host-photo" role="img" aria-label="Portrait photo of host Dorian Weatherall"></div>
  <p class="host-name">Dorian Weatherall</p>
  <p class="host-label">YOUR HOST</p>

  <p class="credit">Created and Hosted by<br>Dorian Weatherall</p>
</main>
</body>
</html>
```